Al Qarmani our website www.klorvin.com

We need a Web Design for a new company called 'KLORVIN'. We develop innovative uPhone applications for consumers. Our initial product is PennyWise - an application that helps people manage their budgets and save money. We would like to see designs that use the color green. The final design should communicate financial safety and growth”.

Target Market(s)

technology and Electrics

Number of Pages Required

1 page

Requirements
Must have
• And work for pomelo and robotix
• To working min 2 languages Arabic and English
Nice to have
Should not have

```html
<!DOCTYPE html>
<html lang="en">
<head>
<meta charset="utf-8">
<title>KLORVIN – Budget Calculator</title>
<link rel="stylesheet" href="https://fonts.googleapis.com/css2?family=Montserrat:wght@400;500;600;700&display=swap">
<style>
:root{
  --green:#7dc242;
  --green-dark:#3f6f1f;
  --green-light:#b5d98c;
  --green-mid:#5fb540;
  --teal:#52cbc6;
  --teal-light:#7ee0dc;
  --ink:#222222;
  --footer:#151515;
  --panel:#f2f2f2;
  --white:#ffffff;
  --text:#333333;
}
*{box-sizing:border-box;margin:0;padding:0}
html,body{width:1200px;height:3185px;overflow:hidden}
body{position:relative;font-family:"Montserrat",Arial,sans-serif;background:var(--white);color:var(--text)}
.abs{position:absolute}

/* top navigation */
.topbar{left:0;top:0;width:1200px;height:47px;background:var(--white)}
.topnav{position:absolute;right:50px;top:0;height:47px;display:flex;align-items:center;gap:32px;font-size:11px;font-weight:500;color:var(--green);text-transform:uppercase;letter-spacing:.3px}
.topnav .lang{display:flex;align-items:center;gap:8px}
.flag{width:18px;height:11px;display:flex}
.flag i{display:block}
.flag .bar{width:5px;background:#d12c2c}
.flag .stripes{flex:1;display:flex;flex-direction:column}
.flag .stripes b{flex:1;display:block}
.social-mini{display:flex;gap:6px}
.social-mini span{width:16px;height:16px;border-radius:50%;background:var(--green);display:block}

/* hero */
.hero{left:0;top:47px;width:1200px;height:700px;background:linear-gradient(120deg,#5fcfae 0%,#8fd46a 45%,#a4d95a 100%)}
.brand{left:81px;top:117px;color:var(--white);font-size:34px;font-weight:700;letter-spacing:6px;display:flex;align-items:center;gap:12px}
.brand .dot{width:16px;height:16px;border-radius:50%;background:var(--white)}
.hero-title{left:0;width:1200px;top:366px;text-align:center;color:var(--white);font-size:46px;font-weight:500;line-height:57px;letter-spacing:.5px}
.btn-outline{left:515px;top:517px;width:168px;height:51px;border:2px solid var(--white);color:var(--white);font-size:14px;font-weight:500;display:flex;align-items:center;justify-content:center;letter-spacing:.5px}
.slider-dots{left:573px;top:624px;display:flex;gap:5px}
.slider-dots span{width:11px;height:11px;border-radius:50%;border:2px solid var(--white)}
.slider-dots span.on{background:var(--white)}

/* how to */
.howto{left:0;top:747px;width:1200px;height:700px;background:var(--ink)}
.howto-title{left:0;width:1200px;top:838px;text-align:center;color:var(--white);font-size:44px;font-weight:400}
.step{width:320px;text-align:center;color:var(--white)}
.step svg{display:block;margin:0 auto}
.step .num{width:36px;height:36px;border:2px solid var(--green);border-radius:50%;color:var(--green);font-size:21px;line-height:32px;margin:39px auto 0}
.step p{margin-top:28px;font-size:25px;font-weight:500;line-height:30px}

/* calculator */
.card{width:468px;height:390px;border:14px solid var(--green);border-radius:10px;background:var(--panel)}
.card::before{content:"";position:absolute;left:50%;top:-38px;margin-left:-24px;border:24px solid transparent;border-bottom:24px solid var(--green);border-top:0}
.field-label{font-size:20px;color:var(--text);position:absolute;left:14px}
.input{position:absolute;left:10px;width:127px;height:36px;border:1.5px solid var(--green);background:var(--white);font-size:18px;padding-left:8px;line-height:33px}
.select{position:absolute;left:156px;width:273px;height:36px;border:1.5px solid var(--green);background:var(--white);font-size:18px;padding-left:9px;line-height:33px}
.select::after{content:"";position:absolute;right:12px;top:14px;border:7px solid transparent;border-top:7px solid var(--green)}
.legend{position:absolute;left:232px;top:62px;list-style:none}
.legend li{display:flex;align-items:center;gap:12px;height:41px;font-size:17.5px;color:var(--text)}
.legend i{width:19px;height:19px;display:block}

/* products */
.products{left:0;top:2085px;width:1200px;height:447px;background:linear-gradient(135deg,#8ccf4a 0%,#9fd64f 50%,#8fcf48 100%)}
.products-title{left:0;width:1200px;top:2240px;text-align:center;color:var(--white);font-size:34px;font-weight:400;letter-spacing:1px}
.products-rule{left:536px;top:2288px;width:162px;height:2px;background:var(--white)}
.products-text{left:235px;width:730px;top:2318px;text-align:center;color:var(--white);font-size:16px;line-height:21px}

.btn-contact{left:506px;top:2632px;width:186px;height:47px;background:var(--teal);color:var(--white);font-size:13px;font-weight:600;display:flex;align-items:center;justify-content:center}

/* footer */
.footer{left:0;top:2781px;width:1200px;height:404px;background:var(--footer);color:var(--white)}
.footer h4{position:absolute;top:60px;font-size:17.5px;font-weight:600;letter-spacing:.5px}
.footer h4::after{content:"";position:absolute;left:0;top:33px;width:72px;height:2px;background:var(--teal)}
.about-text{left:100px;top:2906px;width:210px;font-size:11.5px;line-height:14.3px;color:var(--white)}
.quick{left:336px;top:2900px;list-style:none;font-size:12px;font-weight:600;line-height:25px;color:var(--white)}
.contact-item{left:555px;font-size:12px;line-height:15px;color:var(--white)}
.contact-item .ico{position:absolute;left:0;top:1px}
.contact-item span{display:block;padding-left:14px}
.cb-input{left:792px;width:308px;height:38px;background:var(--white);color:#aaa;font-size:11.5px;padding-left:10px;line-height:38px}
.btn-send{left:792px;top:3081px;width:75px;height:38px;border:2px solid var(--teal);color:var(--white);font-size:12px;display:flex;align-items:center;justify-content:center}
.social{left:100px;top:3081px;display:flex;gap:13px}
.social span{width:38px;height:38px;border-radius:50%;background:var(--teal-light);display:block}
</style>
</head>
<body>

<header class="abs topbar">
  <nav class="topnav">
    <span class="lang"><span class="flag"><i class="bar"></i><span class="stripes"><b style="background:#2e9a45"></b><b style="background:#fff;border-right:1px solid #ddd"></b><b style="background:#111"></b></span></span>Select Language</span>
    <span>Home</span><span>About Us</span><span>Products</span><span>Contact Us</span><span>Login / Signup</span><span>Shops</span>
    <span class="social-mini" aria-label="Social links"><span></span><span></span><span></span></span>
  </nav>
</header>

<section class="abs hero" role="img" aria-label="Photo of a young couple reviewing their budget together at a table, under a green tint"></section>
<div class="abs brand"><span class="dot"></span>KLORVIN</div>
<h1 class="abs hero-title">MANAGE YOUR BUDGETS<br>AND SAVE MONEY</h1>
<div class="abs btn-outline">LEARN MORE</div>
<div class="abs slider-dots"><span class="on"></span><span></span><span></span></div>

<section class="abs howto"></section>
<h2 class="abs howto-title">How to use our Budget Calculator</h2>

<div class="abs step" style="left:80px;top:996px">
  <svg width="158" height="158" viewBox="0 0 158 158"><circle cx="79" cy="79" r="76" fill="none" stroke="#7dc242" stroke-width="4"/><rect x="44" y="44" width="14" height="26" rx="2" fill="#7dc242"/><path d="M50 66 L78 66 Q90 66 94 76 L100 92 L82 98 L60 86 Z" fill="#7dc242"/><circle cx="104" cy="106" r="13" fill="none" stroke="#7dc242" stroke-width="4"/><text x="104" y="112" font-size="16" font-weight="700" fill="#7dc242" text-anchor="middle" font-family="Montserrat,sans-serif">$</text></svg>
  <div class="num">1</div>
  <p>Enter what you<br>spend and how much<br>you earn</p>
</div>
<div class="abs step" style="left:440px;top:996px">
  <svg width="158" height="158" viewBox="0 0 158 158"><circle cx="79" cy="79" r="76" fill="none" stroke="#7dc242" stroke-width="4"/><rect x="50" y="42" width="58" height="76" rx="6" fill="#7dc242"/><rect x="66" y="36" width="26" height="12" rx="3" fill="#7dc242" stroke="#222" stroke-width="3"/><g fill="#222"><rect x="60" y="62" width="7" height="7"/><rect x="72" y="63" width="28" height="5"/><rect x="60" y="78" width="7" height="7"/><rect x="72" y="79" width="28" height="5"/><rect x="60" y="94" width="7" height="7"/><rect x="72" y="95" width="28" height="5"/></g></svg>
  <div class="num">2</div>
  <p>The calculator will<br>give you a breakdown<br>of your finances.</p>
</div>
<div class="abs step" style="left:778px;top:996px">
  <svg width="158" height="158" viewBox="0 0 158 158"><circle cx="79" cy="79" r="76" fill="none" stroke="#7dc242" stroke-width="4"/><circle cx="79" cy="58" r="22" fill="none" stroke="#7dc242" stroke-width="5"/><text x="79" y="68" font-size="28" font-weight="700" fill="#7dc242" text-anchor="middle" font-family="Montserrat,sans-serif">$</text><path d="M36 78 Q40 108 70 118 L70 104 Q52 96 48 80 Z" fill="#7dc242"/><path d="M122 78 Q118 108 88 118 L88 104 Q106 96 110 80 Z" fill="#7dc242"/></svg>
  <div class="num">3</div>
  <p>personalised tips to<br>help you make<br>the most of your money</p>
</div>

<section class="abs card" style="left:104px;top:1564px">
  <span class="field-label" style="top:30px">Pay (after tax)</span>
  <span class="input" style="top:64px">0.00</span><span class="select" style="top:64px">per Month</span>
  <span class="field-label" style="top:143px">Income from self-employment</span>
  <span class="input" style="top:177px">0.00</span><span class="select" style="top:177px">per Year</span>
  <span class="field-label" style="top:254px">Statutory Sick Pay</span>
  <span class="input" style="top:288px">0.00</span><span class="select" style="top:288px">per Month</span>
</section>

<section class="abs card" style="left:626px;top:1564px">
  <svg class="abs" style="left:21px;top:82px" width="200" height="200" viewBox="0 0 200 200">
    <g transform="rotate(-90 100 100)" fill="none" stroke-width="43">
      <circle cx="100" cy="100" r="72.5" stroke="#7dc242" stroke-dasharray="173 456"/>
      <circle cx="100" cy="100" r="72.5" stroke="#3f6f1f" stroke-dasharray="73 456" stroke-dashoffset="-173"/>
      <circle cx="100" cy="100" r="72.5" stroke="#b5d98c" stroke-dasharray="14 456" stroke-dashoffset="-246"/>
      <circle cx="100" cy="100" r="72.5" stroke="#52cbc6" stroke-dasharray="196 456" stroke-dashoffset="-260"/>
    </g>
  </svg>
  <ul class="legend">
    <li><i style="background:var(--green-dark)"></i>Household bills</li>
    <li><i style="background:var(--green)"></i>Living Costs</li>
    <li><i style="background:var(--green-light)"></i>Finance,Insurance</li>
    <li><i style="background:var(--green-mid)"></i>Family &amp; Friends</li>
    <li><i style="background:var(--teal)"></i>Travel</li>
    <li><i style="background:var(--teal-light)"></i>Leisure</li>
  </ul>
</section>

<section class="abs products" role="img" aria-label="Green-tinted background of financial charts, a calculator and a pen"></section>
<h2 class="abs products-title">PRODUCTS</h2>
<div class="abs products-rule"></div>
<p class="abs products-text">Our valuable product allow us to simplify to manage the complex process of budget<br>from the ground up, without losing sight of our primary goal: excellence.</p>

<div class="abs btn-contact">CONTACT US</div>

<footer class="abs footer">
  <h4 style="left:100px">ABOUT US</h4>
  <h4 style="left:336px">QUICK LINKS</h4>
  <h4 style="left:555px">CONTACT DETAILS</h4>
  <h4 style="left:792px">REQUEST CALLBACK</h4>
</footer>
<p class="abs about-text">Sample company is a leading-edge land development company with more than 25 years of experience. We are a dedicated team of driven industry experts that rivals the largest developers in the Nation with a streamlined and nimble operation which enables us to provide a competitive advantage.</p>
<ul class="abs quick"><li>HOME</li><li>ABOUT US</li><li>PRODUCTS</li><li>CONTACT US</li><li>CONTACT US</li><li>CONTACT US</li></ul>

<div class="abs contact-item" style="top:2900px">
  <svg class="ico" width="9" height="12" viewBox="0 0 9 12"><path d="M4.5 0A4.5 4.5 0 0 0 0 4.5C0 8 4.5 12 4.5 12S9 8 9 4.5A4.5 4.5 0 0 0 4.5 0Z" fill="#fff"/><circle cx="4.5" cy="4.5" r="1.6" fill="#151515"/></svg>
  <span>ADDRESS</span><span>4580 Palm Grove Rd.</span><span>Alden FL 30412</span>
</div>
<div class="abs contact-item" style="top:2959px">
  <svg class="ico" width="10" height="10" viewBox="0 0 10 10"><path d="M2 0L4 2.5 3 4Q4 6 6 7L7.5 6 10 8 8 10Q2 9 0 2Z" fill="#fff"/></svg>
  <span>PHONE</span><span>+1 555.014.2290</span>
</div>
<div class="abs contact-item" style="top:3002px">
  <svg class="ico" width="10" height="8" viewBox="0 0 10 8"><rect width="10" height="8" fill="#fff"/><path d="M0 0L5 4.5 10 0" fill="none" stroke="#151515" stroke-width="1"/></svg>
  <span>E-MAIL</span><span>info@klorvin.com</span>
</div>

<div class="abs cb-input" style="top:2894px">Your Name</div>
<div class="abs cb-input" style="top:2957px">Your Email</div>
<div class="abs cb-input" style="top:3020px">Your Contact</div>
<div class="abs btn-send">Send</div>

<div class="abs social" aria-label="Social network links"><span></span><span></span><span></span></div>

</body>
</html>
```